Accounting Practice Business Card Design

I have a logo I am happy for you to use in the design of the Business Card.
You can edit and change colours as you please, I am not fixated on it.
I am looking for a modern and clean overall feel for the finished design.

The business is a small accounting practice who thrives on word of mouth referrals and this card will be given to all current and prospect clients.

Industry/Entity Type

Accountant

Contact Information for Business Card

Marcus Elwin
Level 5, 8 Corvale Ridge Road
ASHGROVE RISE VIC 3187
Phone: 9481 3057
Email: melwin@mrfaccountants.com.au
Web: www.mrfaccountants.com.au

Font styles to use
Serif
Sans Serif

Colors
0555a3
3277b5
85acd3
0393ce
33a6d7
85cae6
00a990
33b8a4
9bcb3c

Requirements
Must have
• "The end to your tax problems begin with us"
• "A referral from you is our greatest compliment"
Nice to have
• Modern clean professional

```html
<!DOCTYPE html>
<html lang="en">
<head>
<meta charset="utf-8">
<title>MRF Accountants – Business Card</title>
<link rel="stylesheet" href="https://fonts.googleapis.com/css2?family=Lato:wght@400;700;900&family=Oswald:wght@600&display=swap">
<style>
  :root {
    --brand-blue: #255b9a;
    --accent-blue: #85bde0;
    --paper: #f7f8f9;
    --ink: #555a60;
    --divider: #b8bcc0;
    --backdrop: #e9eaeb;
  }
  * { box-sizing: border-box; margin: 0; padding: 0; }
  html, body { width: 1200px; height: 1146px; overflow: hidden; }
  body {
    background: var(--backdrop);
    font-family: "Lato", sans-serif;
    display: flex;
    flex-direction: column;
    align-items: center;
    justify-content: center;
    gap: 70px;
  }
  .card {
    position: relative;
    width: 840px;
    height: 480px;
    overflow: hidden;
    box-shadow: 0 6px 18px rgba(0,0,0,0.12);
  }

  /* Front */
  .card--front { background: var(--paper); }
  .wordmark {
    font-family: "Lato", sans-serif;
    font-weight: 900;
    letter-spacing: 1.5px;
    display: flex;
    align-items: center;
    gap: 12px;
    white-space: nowrap;
  }
  .wordmark__square { width: 22px; height: 22px; flex: none; }
  .card--front .wordmark {
    position: absolute;
    left: 50px; top: 192px;
    width: 350px;
    font-size: 26px;
    color: var(--brand-blue);
  }
  .card--front .wordmark__square { background: var(--accent-blue); }
  .divider {
    position: absolute;
    left: 430px; top: 95px;
    width: 1px; height: 230px;
    background: var(--divider);
  }
  .contact {
    position: absolute;
    left: 470px; top: 92px;
    color: var(--ink);
  }
  .contact__name {
    font-family: "Oswald", sans-serif;
    font-weight: 600;
    font-size: 34px;
    color: var(--brand-blue);
    letter-spacing: 1px;
    margin-bottom: 18px;
  }
  .contact__address { font-size: 19px; line-height: 1.35; margin-bottom: 10px; }
  .contact__list { list-style: none; font-size: 19px; line-height: 1.5; }
  .contact__list li { display: flex; align-items: center; gap: 10px; }
  .contact__list svg { width: 18px; height: 18px; flex: none; }

  .band {
    position: absolute;
    left: 0; right: 0; bottom: 0;
    display: flex;
    align-items: center;
    padding-left: 60px;
    font-weight: 700;
    font-size: 20px;
    letter-spacing: 2.5px;
    text-transform: uppercase;
    border-top: 7px solid var(--accent-blue);
  }
  .card--front .band {
    height: 84px;
    background: var(--brand-blue);
    color: #ffffff;
  }

  /* Back */
  .card--back { background: var(--brand-blue); }
  .card--back .wordmark {
    position: absolute;
    left: 0; right: 0; top: 165px;
    justify-content: center;
    font-size: 44px;
    letter-spacing: 2px;
    color: #ffffff;
  }
  .card--back .wordmark__square { background: var(--accent-blue); width: 34px; height: 34px; }
  .card--back .band {
    height: 84px;
    background: var(--paper);
    color: var(--brand-blue);
  }
</style>
</head>
<body>

<section class="card card--front">
  <div class="wordmark"><span class="wordmark__square"></span>MRF ACCOUNTANTS</div>
  <div class="divider"></div>
  <div class="contact">
    <h1 class="contact__name">MARCUS ELWIN</h1>
    <p class="contact__address">Level 5, 8 Corvale Ridge Road<br>Ashgrove Rise Vic 3187</p>
    <ul class="contact__list">
      <li>
        <svg viewBox="0 0 24 24" aria-hidden="true"><path d="M6.6 10.8a15 15 0 0 0 6.6 6.6l2.2-2.2a1 1 0 0 1 1-.25 11.4 11.4 0 0 0 3.6.6 1 1 0 0 1 1 1V20a1 1 0 0 1-1 1A17 17 0 0 1 3 4a1 1 0 0 1 1-1h3.5a1 1 0 0 1 1 1c0 1.25.2 2.45.6 3.6a1 1 0 0 1-.25 1z" fill="#555a60"/></svg>
        9481 3057
      </li>
      <li>
        <svg viewBox="0 0 24 24" aria-hidden="true"><rect x="2.5" y="5" width="19" height="14" fill="none" stroke="#555a60" stroke-width="1.8"/><path d="M2.5 5l9.5 8 9.5-8" fill="none" stroke="#555a60" stroke-width="1.8"/></svg>
        melwin@mrfaccountants.com.au
      </li>
      <li>
        <svg viewBox="0 0 24 24" aria-hidden="true"><g fill="none" stroke="#555a60" stroke-width="1.6"><circle cx="12" cy="12" r="9"/><ellipse cx="12" cy="12" rx="4" ry="9"/><path d="M3 12h18M4.5 7.5h15M4.5 16.5h15"/></g></svg>
        www.mrfaccountants.com.au
      </li>
    </ul>
  </div>
  <div class="band">A referral from you is our greatest compliment.</div>
</section>

<section class="card card--back">
  <div class="wordmark"><span class="wordmark__square"></span>MRF ACCOUNTANTS</div>
  <div class="band">The end to your tax problems begin with us.</div>
</section>

</body>
</html>
```